Birchwood Lodge Rentals Bill Board

7x21 bill board.

Im needing a bill board for a vacation rental company. Specializing in cabin rentals.
Here are the main points I want mentioned on the billboard:

Quality vacation rentals

Accepting new vacation rental homes.

Family owned and operated.

Fernridgestays.com
865-417-3082

Use either logo whichever looks best. Be creative

Target Market(s)

Cabin owners

Industry/Entity Type

Hospitality

Font styles to use
Sans Serif

Requirements
Must have
• Would like the cabin picture to be the background. Must have the fernridge logo, phone number and website

```html
<!DOCTYPE html>
<html lang="en">
<head>
<meta charset="utf-8">
<title>Birchwood Lodge Rentals Billboard</title>
<link href="https://fonts.googleapis.com/css2?family=Archivo+Black&family=Roboto+Condensed:wght@400;600;700&display=swap" rel="stylesheet">
<style>
  :root {
    --navy: #2e4356;
    --orange: #f9a22b;
    --orange-light: #fbb13d;
    --white: #ffffff;
    --ink: #111111;
    --stage: #eef1f4;
    --wood: #c07a3a;
    --dusk: #e9b27a;
    --pine: #5b6a5a;
  }
  html, body {
    margin: 0;
    padding: 0;
    width: 1200px;
    height: 900px;
    overflow: hidden;
    background: var(--stage);
  }
  .billboard {
    position: absolute;
    left: 40px;
    top: 310px;
    width: 1120px;
    height: 280px;
    display: block;
    box-shadow: 0 6px 18px rgba(0,0,0,0.15);
  }
  .headline {
    font-family: "Archivo Black", "Arial Black", sans-serif;
    fill: var(--navy);
  }
  .condensed {
    font-family: "Roboto Condensed", "Arial Narrow", sans-serif;
  }
  .brand-name {
    font-family: "Roboto Condensed", "Arial Narrow", sans-serif;
    font-weight: 600;
    fill: var(--white);
  }
  .tagline { fill: var(--ink); font-weight: 400; }
  .badge-text { fill: var(--ink); font-weight: 700; }
  .contact { fill: var(--white); font-weight: 600; }
</style>
</head>
<body>
<svg class="billboard" viewBox="0 0 1680 420" xmlns="http://www.w3.org/2000/svg">
  <defs>
    <linearGradient id="cabin-tones" x1="0" y1="0" x2="1" y2="1">
      <stop offset="0" stop-color="var(--dusk)"/>
      <stop offset="0.45" stop-color="var(--wood)"/>
      <stop offset="1" stop-color="var(--pine)"/>
    </linearGradient>
    <linearGradient id="travel-tones" x1="0" y1="0" x2="1" y2="0">
      <stop offset="0" stop-color="#dfe5ea"/>
      <stop offset="1" stop-color="#ffffff"/>
    </linearGradient>
  </defs>

  <rect class="panel" width="1680" height="420" fill="var(--white)"/>

  <path class="cabin-photo" role="img" aria-label="Photo of a large log cabin with lit windows and decks on a mountain hillside at sunset"
        d="M1000 0 H1680 V420 H1320 Z" fill="url(#cabin-tones)"/>

  <path class="accent-sweep" d="M670 0 H1055 L1205 292 Q1212 304 1195 304 H1000 Q965 304 945 284 Z" fill="var(--orange)"/>
  <path class="accent-line" d="M640 0 L938 292 Q965 318 1005 320 H1235" fill="none" stroke="var(--orange)" stroke-width="5"/>

  <rect class="badge" x="770" y="8" width="305" height="180" rx="45" fill="var(--orange-light)"/>
  <text class="condensed badge-text" text-anchor="middle" font-size="38">
    <tspan x="917" y="60" textLength="243" lengthAdjust="spacingAndGlyphs">Family Owned</tspan>
    <tspan x="921" y="95">and</tspan>
    <tspan x="927" y="130" textLength="158" lengthAdjust="spacingAndGlyphs">Operated</tspan>
  </text>

  <path class="logo-stripe" d="M0 0 H330 Q260 100 190 110 H0 Z" fill="var(--orange)"/>
  <path class="logo-band" d="M0 0 H315 Q250 75 185 85 H0 Z" fill="var(--navy)"/>
  <text class="brand-name" x="30" y="52" font-size="20" textLength="208" lengthAdjust="spacingAndGlyphs">BIRCHWOOD LODGE RENTALS</text>

  <path class="top-tab" d="M345 0 H485 L440 32 Q415 48 390 32 Z" fill="var(--orange)"/>

  <text class="headline" x="390" y="175" text-anchor="middle" font-size="68" textLength="675" lengthAdjust="spacingAndGlyphs">Quality Vacation</text>
  <text class="headline" x="402" y="243" text-anchor="middle" font-size="68" textLength="381" lengthAdjust="spacingAndGlyphs">RENTALS</text>
  <text class="condensed tagline" x="404" y="285" text-anchor="middle" font-size="38" textLength="648" lengthAdjust="spacingAndGlyphs">Accepting New Vacation Rental Homes</text>

  <rect class="travel-doodles" role="img" aria-label="Line icons of a palm tree, compass, map pin and airplane along a dashed travel route"
        x="0" y="300" width="360" height="120" fill="url(#travel-tones)"/>

  <path class="contact-band" d="M578 420 C640 360 700 285 790 285 H1225 L1405 420 Z" fill="var(--navy)"/>
  <text class="condensed contact" x="655" y="380" font-size="38" textLength="310" lengthAdjust="spacingAndGlyphs">Fernridgestays.com</text>
  <text class="condensed contact" x="1005" y="380" font-size="38" textLength="235" lengthAdjust="spacingAndGlyphs">865-417-3082</text>
</svg>
</body>
</html>
```